Post card selling a software for elderly visitor security

I need a postcard re-design that will entice children of elderly parents to sign-up to monitor the visitors (via online reporting dashboard) that care for them. These elderly residents live in a nursing home and many can't remember who came in the room to care for them. This is a major safety and security issue and adult children sometimes have no way of knowing who is visiting their parents. Our software provides an online reporting dashboard and sends text messages to adult children when a visitor arrives at the nursing home.

Target Market(s)

women between 50-65

Industry/Entity Type

Nursing Home

Colors

Designer to choose colors to be used in the design.

Requirements
Must have
• Must have Two questions: Are you the Primary Guardian of a resident in this community? If so, would you like to know who is visiting them?
• Must have a desktop computer and phone
• Needs to have a white background

```html
<!DOCTYPE html>
<html lang="en">
<head>
<meta charset="utf-8">
<title>Visitrail Postcard</title>
<link href="https://fonts.googleapis.com/css2?family=Catamaran:wght@500;600;700&family=Libre+Baskerville&display=swap" rel="stylesheet">
<style>
:root{
  --white:#ffffff;
  --ink-navy:#163b5e;
  --rule:#9fb4c4;
  --band:#1c86c8;
  --band-dark:#0f5597;
  --band-light:#35a6e0;
  --photo-top:#f7faf9;
  --photo-bottom:#e4eeec;
  --bezel:#111418;
  --silver:#d9dbde;
  --silver-dark:#a9adb2;
  --panel:#f1f2f4;
  --ink:#33363b;
  --accent:#2f8fd8;
  --bubble:#dfeaea;
  --bubble-edge:#9a5a2c;
  --bubble-text:#8a4a1e;
  --badge-ring:#7fa8bd;
  --badge-inner:#f3f6f7;
  --badge-ink:#4f5f68;
  --badge-band:#f2c240;
}
*{box-sizing:border-box;margin:0;padding:0}
html,body{width:1200px;height:811px;overflow:hidden;background:var(--white)}
.postcard{position:relative;width:1200px;height:811px;overflow:hidden;font-family:"Catamaran",sans-serif;background:var(--white)}
.hero-photo{position:absolute;left:0;top:0;width:1200px;height:588px;background:linear-gradient(180deg,var(--photo-top),var(--photo-bottom))}
.question{position:absolute;left:0;width:1200px;text-align:center;color:var(--ink-navy);font-weight:500;font-size:62px;line-height:64px}
.question-one{top:68px}
.question-two{top:255px}
.divider{position:absolute;left:169px;top:229px;width:857px;height:1px;background:var(--rule)}
.blue-band{position:absolute;left:0;top:588px;width:1200px;height:223px}
.monitor{position:absolute;left:75px;top:419px;width:450px}
.monitor-frame{width:450px;height:268px;background:var(--bezel);border-radius:10px 10px 0 0;padding:17px 18px 0 18px}
.screen{position:relative;width:414px;height:234px;background:linear-gradient(180deg,#2aa0e0,#3a70c0);overflow:hidden}
.chin{width:450px;height:43px;background:linear-gradient(var(--silver),var(--silver-dark));border-radius:0 0 8px 8px}
.stand{margin:0 auto;width:120px;height:53px;background:linear-gradient(var(--silver-dark),var(--silver));clip-path:polygon(22% 0,78% 0,100% 100%,0 100%)}
.sidebar{position:absolute;left:58px;top:20px;width:14px;height:214px;background:#2b3440}
.dash{position:absolute;left:72px;top:20px;width:286px;height:214px;background:var(--panel);color:var(--ink);font-family:"Libre Baskerville",serif}
.browser-bar{position:absolute;left:58px;top:0;width:300px;height:20px;background:#fbfbfb;border-bottom:1px solid #ddd}
.dash-title{position:absolute;left:8px;top:6px;font-size:9px}
.dash-sub{position:absolute;left:8px;top:19px;font-size:5px}
.dash-label{position:absolute;left:8px;font-size:5px}
.field{position:absolute;height:7px;background:var(--white);border:1px solid #ccc}
.btn{position:absolute;height:7px;background:var(--accent)}
.export-box{position:absolute;left:6px;top:72px;width:272px;height:38px;background:var(--white);border:1px solid #ddd}
.export-box span{position:absolute;left:4px;top:4px;font-size:6px}
.table-head,.table-row{position:absolute;left:6px;width:272px;font-family:Arial,sans-serif;font-size:3.6px;display:flex;gap:5px;padding:2px 4px}
.table-head{top:120px;font-weight:bold;background:#fff}
.table-row{background:#fff;border-top:1px solid #e4e4e4}
.table-row.active{background:#fff7d6}
.photos-pop{position:absolute;left:183px;top:142px;width:229px;height:90px;background:var(--white);border:1px solid #3a6fc0}
.photos-pop h4{position:absolute;left:4px;top:3px;font:400 7px Arial,sans-serif;color:#222}
.photos-pop p{position:absolute;left:4px;top:13px;font:3.6px Arial,sans-serif;color:#444}
.visitor-photo{position:absolute;top:22px;width:72px;height:64px;background:linear-gradient(180deg,#e8eef2,#8fb8d8)}
.pointer{position:absolute;left:0;top:0}
.phone{position:absolute;left:537px;top:550px;width:113px;height:237px;background:var(--white);border:1px solid #cfd3d6;border-radius:16px}
.phone-screen{position:absolute;left:6px;top:28px;width:99px;height:176px;background:linear-gradient(180deg,#0c2a2c,#1e4a3e 35%,#7a8a78 60%,#d79a52)}
.notice{position:absolute;left:2px;top:52px;width:95px;height:22px;background:rgba(255,255,255,.9);border-radius:3px;font:3.5px Arial,sans-serif;color:#555;padding:2px}
.reply{position:absolute;left:2px;top:76px;width:95px;height:10px;background:rgba(160,210,190,.9);border-radius:2px;font:4px Arial,sans-serif;text-align:center;line-height:10px;color:#333}
.home-key{position:absolute;left:48px;top:211px;width:16px;height:16px;border:1px solid #aaa;border-radius:50%}
.speaker{position:absolute;left:45px;top:14px;width:22px;height:2px;background:#333;border-radius:1px}
.bubble{position:absolute;background:var(--bubble);border:4px solid var(--bubble-edge);border-radius:10px;color:var(--bubble-text);font-weight:500;font-size:14px;line-height:16px;text-align:center;display:flex;align-items:center;justify-content:center}
.bubble-arrived{left:824px;left:634px;top:497px;width:119px;height:73px}
.bubble-left{left:649px;top:597px;width:119px;height:75px}
.trial-badge{position:absolute;left:849px;top:429px;width:260px;height:260px;border-radius:50%;background:var(--badge-inner);border:14px solid var(--badge-ring);text-align:center;color:var(--badge-ink)}
.trial-days{position:absolute;left:0;top:38px;width:100%;font-size:46px;font-weight:700;line-height:46px}
.trial-label{position:absolute;left:-20px;top:98px;width:272px;height:50px;background:var(--badge-band);color:var(--white);font-size:38px;font-weight:700;line-height:54px}
.trial-note{position:absolute;left:0;top:160px;width:100%;font-size:24px;font-weight:700;line-height:26px}
</style>
</head>
<body>
<main class="postcard">
  <div class="hero-photo" role="img" aria-label="Photo of a caregiver in scrubs helping an elderly man and woman in a garden"></div>

  <h1 class="question question-one">Are you the Primary Guardian of a<br>resident in this community ?</h1>
  <div class="divider"></div>
  <h2 class="question question-two">If so, would you like to know who<br>is visiting them ?</h2>

  <svg class="blue-band" viewBox="0 0 1200 223" aria-hidden="true">
    <rect width="1200" height="223" fill="var(--band)"/>
    <path d="M0 50 C60 20 140 60 190 130 C230 190 160 223 120 223 L0 223Z" fill="var(--band-light)"/>
    <path d="M1000 223 C980 160 1060 130 1120 150 C1170 165 1200 140 1200 110 L1200 223Z" fill="var(--band-light)" opacity=".8"/>
    <path d="M0 223 L0 160 C200 190 400 140 560 200 L560 223Z" fill="var(--band-dark)" opacity=".35"/>
  </svg>

  <div class="monitor">
    <div class="monitor-frame">
      <div class="screen">
        <div class="browser-bar"></div>
        <div class="sidebar"></div>
        <div class="dash">
          <div class="dash-title">Visitrail Visitor Dashboard</div>
          <div class="dash-sub">for XYZ Senior Living</div>
          <svg style="position:absolute;left:232px;top:4px" width="52" height="24" viewBox="0 0 52 24" aria-hidden="true">
            <circle cx="12" cy="12" r="10" fill="#e05a8a"/><path d="M12 12 L12 2 A10 10 0 0 1 22 12Z" fill="#3aa0d8"/><path d="M12 12 L22 12 A10 10 0 0 1 4 18Z" fill="#2cb89a"/>
            <circle cx="40" cy="12" r="10" fill="#e8a030"/><circle cx="40" cy="12" r="5" fill="var(--panel)"/><path d="M40 2 A10 10 0 0 1 50 12 L45 12 A5 5 0 0 0 40 7Z" fill="#b040a0"/>
          </svg>
          <div class="dash-label" style="top:36px">Search for Events</div>
          <div class="field" style="left:8px;top:48px;width:40px"></div>
          <div class="field" style="left:56px;top:48px;width:40px"></div>
          <div class="field" style="left:104px;top:48px;width:40px"></div>
          <div class="field" style="left:152px;top:48px;width:60px"></div>
          <div class="btn" style="left:218px;top:48px;width:16px"></div>
          <div class="export-box"><span>Export Visits</span><div class="btn" style="left:4px;top:16px;width:26px"></div></div>
          <div class="table-head"><span>Date</span><span>Sign In</span><span>Sign Out</span><span>Minutes</span><span>Visitor</span><span>Phone</span><span>Status</span><span>Type</span><span>Device</span><span>Company</span><span>Resident</span></div>
          <div class="table-row active" style="top:131px"><span>12/31 11:01 PM</span><span>In Progress</span><span>Maya Reyes</span></div>
          <div class="table-row" style="top:158px"><span>12/31 10:51 PM</span><span>7:19 AM</span><span>509</span><span>Nora Hale</span></div>
          <div class="table-row" style="top:185px"><span>12/31 10:23 PM</span><span>4:01 AM</span><span>459</span><span>Ben Ortiz</span></div>
        </div>
        <div class="photos-pop">
          <h4>Visitor Photos</h4>
          <p>Photos of Maya Reyes taken during sign-in on 12/31 at 11:01 PM</p>
          <div class="visitor-photo" role="img" aria-label="Visitor sign-in photo" style="left:32px"></div>
          <div class="visitor-photo" role="img" aria-label="Visitor sign-in photo" style="left:152px"></div>
        </div>
        <svg class="pointer" width="414" height="234" aria-hidden="true"><line x1="213" y1="204" x2="190" y2="176" stroke="#e02020" stroke-width="1.2"/><path d="M188 173 L194 176 L190 180Z" fill="#e02020"/></svg>
      </div>
    </div>
    <div class="chin"></div>
    <div class="stand"></div>
  </div>

  <div class="phone">
    <div class="speaker"></div>
    <div class="phone-screen">
      <div class="notice">NEW NOTIFICATION · visitor signed in</div>
      <div class="reply">Reply</div>
    </div>
    <div class="home-key"></div>
  </div>

  <div class="bubble bubble-arrived">Dr. Lane arrived<br>to see mom</div>
  <div class="bubble bubble-left">Dad left the<br>community</div>

  <div class="trial-badge">
    <div class="trial-days">30-DAY</div>
    <div class="trial-label">Free Trial</div>
    <div class="trial-note">NO RISK!</div>
  </div>
</main>
</body>
</html>
```